Corvanta512 Business Card Redesign

I want to create a design for brand new business cards, I need something exceptional for clear plastic business card design. Please do not submit without it being on a clear design. Photos of the various logo versions attached.

```html
<!DOCTYPE html>
<html lang="en">
<head>
<meta charset="utf-8">
<title>Corvanta512 – Clear Business Card</title>
<link rel="stylesheet" href="https://fonts.googleapis.com/css2?family=Lato:wght@400;700;900&display=swap">
<style>
  :root {
    --page-bg: #b9ada4;
    --clear-tint: rgba(255, 255, 255, 0.30);
    --clear-edge: rgba(255, 255, 255, 0.75);
    --clear-rim: rgba(120, 110, 108, 0.45);
    --frost: rgba(255, 255, 255, 0.78);
    --navy: #1c2747;
    --gold: #a57a3a;
    --gold-light: #c9a262;
    --ink: #1f2228;
    --icon: #ffffff;
  }
  * { margin: 0; padding: 0; box-sizing: border-box; }
  html, body {
    width: 1200px;
    height: 900px;
    overflow: hidden;
    background: var(--page-bg);
    font-family: "Lato", Arial, sans-serif;
  }
  .card {
    position: absolute;
    left: 214px;
    top: 228px;
    width: 772px;
    height: 443px;
    border-radius: 16px;
    background:
      linear-gradient(100deg, rgba(255,255,255,0.38) 0%, rgba(255,255,255,0.22) 50%, rgba(255,255,255,0.34) 100%),
      var(--clear-tint);
    backdrop-filter: blur(3px) saturate(1.1);
    border: 1px solid var(--clear-edge);
    box-shadow:
      inset 0 0 0 1px rgba(255, 255, 255, 0.35),
      inset 0 -2px 0 var(--clear-rim),
      0 4px 12px rgba(60, 50, 45, 0.18);
    overflow: hidden;
  }
  .card-frost {
    position: absolute;
    left: -20px;
    top: -20px;
    width: 300px;
    height: 483px;
    background:
      radial-gradient(ellipse 65% 55% at 50% 55%, var(--frost) 0%, rgba(255,255,255,0.55) 55%, rgba(255,255,255,0) 100%);
    filter: blur(6px);
  }
  .card-frost.right {
    left: 230px;
    width: 230px;
    background:
      radial-gradient(ellipse 60% 60% at 40% 50%, rgba(255,255,255,0.6) 0%, rgba(255,255,255,0.3) 60%, rgba(255,255,255,0) 100%);
  }
  .brand {
    position: absolute;
    left: 0;
    top: 0;
    width: 393px;
    height: 100%;
  }
  .brand-dot {
    position: absolute;
    left: 155px;
    top: 120px;
    width: 120px;
    height: 120px;
    border-radius: 50%;
    background: var(--gold-light);
  }
  .brand-name {
    position: absolute;
    left: 0;
    width: 100%;
    top: 272px;
    text-align: center;
    font-weight: 900;
    font-size: 44px;
    letter-spacing: 1px;
    color: var(--gold);
  }
  .info-band {
    position: absolute;
    left: 393px;
    top: 46px;
    width: 35px;
    height: 350px;
    background: var(--navy);
    border-radius: 35px 0 0 35px;
  }
  .info-accent {
    position: absolute;
    left: 428px;
    top: 69px;
    width: 7px;
    height: 40px;
    background: var(--gold);
    border-radius: 0 4px 4px 0;
  }
  .icon {
    position: absolute;
    left: 403px;
    width: 15px;
    height: 15px;
    fill: var(--icon);
  }
  .holder-name {
    position: absolute;
    left: 458px;
    top: 72px;
    font-weight: 900;
    font-size: 33px;
    letter-spacing: 0.5px;
    color: var(--navy);
  }
  .holder-title {
    position: absolute;
    left: 458px;
    top: 115px;
    font-size: 18px;
    color: var(--gold);
  }
  .contact-line {
    position: absolute;
    left: 458px;
    font-size: 17.5px;
    line-height: 20px;
    color: var(--ink);
  }
</style>
</head>
<body>
  <section class="card" aria-label="Clear frosted plastic business card">
    <div class="card-frost"></div>
    <div class="card-frost right"></div>

    <div class="brand">
      <span class="brand-dot"></span>
      <div class="brand-name">Corvanta512</div>
    </div>

    <div class="info-band"></div>
    <div class="info-accent"></div>

    <svg class="icon" style="top:163px" viewBox="0 0 16 16" aria-label="Address"><path d="M8 0a5.5 5.5 0 0 0-5.5 5.5C2.5 10 8 16 8 16s5.5-6 5.5-10.5A5.5 5.5 0 0 0 8 0zm0 8a2.5 2.5 0 1 1 0-5 2.5 2.5 0 0 1 0 5z"/></svg>
    <svg class="icon" style="top:223px" viewBox="0 0 16 16" aria-label="Phone"><path d="M3.6 1l2.3 2.9-1.4 1.8c.9 2 2.6 3.7 4.8 4.8l1.8-1.4L14 11.4 12.7 15C6.4 14.6 1.4 9.6 1 3.3z"/></svg>
    <svg class="icon" style="top:250px" viewBox="0 0 16 16" aria-label="Mobile"><path d="M4 0h8a1 1 0 0 1 1 1v14a1 1 0 0 1-1 1H4a1 1 0 0 1-1-1V1a1 1 0 0 1 1-1zm1 2v10h6V2zm3 11a1 1 0 1 0 0 2 1 1 0 0 0 0-2z"/></svg>
    <svg class="icon" style="top:276px" viewBox="0 0 16 16" aria-label="Fax"><path d="M4 0h8v4H4zM1 5h14v7h-3v-2H4v2H1zm3 6h8v5H4z"/></svg>
    <svg class="icon" style="top:303px" viewBox="0 0 16 16" aria-label="Email"><path d="M0 3h16v1.2L8 9 0 4.2zm0 2.6l8 4.8 8-4.8V13H0z"/></svg>
    <svg class="icon" style="top:330px" viewBox="0 0 16 16" aria-label="Website"><path d="M8 0a8 8 0 1 0 0 16A8 8 0 0 0 8 0zm0 1.5c.8 0 1.7 1.9 2 4.5H6c.3-2.6 1.2-4.5 2-4.5zM1.6 7.2h3.2c0 .6 0 1.1.1 1.6H1.6a6.5 6.5 0 0 1 0-1.6zm4.4 0h4c0 .6 0 1.1-.1 1.6H6.1c0-.5-.1-1-.1-1.6zm5.2 0h3.2a6.5 6.5 0 0 1 0 1.6h-3.3c.1-.5.1-1 .1-1.6zM6 10h4c-.3 2.6-1.2 4.5-2 4.5S6.3 12.6 6 10z"/></svg>

    <div class="holder-name">DANIEL HART</div>
    <div class="holder-title">Founder &amp; CEO</div>

    <div class="contact-line" style="top:160px">Street Address Here, City</div>
    <div class="contact-line" style="top:187px">State, Country, ZIP 123</div>
    <div class="contact-line" style="top:220px">(123) 456-7890</div>
    <div class="contact-line" style="top:247px">(123) 456-7890</div>
    <div class="contact-line" style="top:273px">(123) 456-7890</div>
    <div class="contact-line" style="top:300px">info@yourwebsitehere.com</div>
    <div class="contact-line" style="top:327px">yourwebsitehere.com</div>
  </section>
</body>
</html>
```